QDN Business Cards

I would like to use deep red (See attached logo), medium grays and white on the card to be used as separators for information using a white font over the red and gray colors. We are a web application design and development firm - specializing in custom software development with a content management solution. Our card needs to reflect innovative and cutting edge company.
I have attached the current card for content purposes - there is a front and back to the card. Open to suggestions on layout.

```html
<!DOCTYPE html>
<html lang="en">
<head>
<meta charset="utf-8">
<title>QDN Tech Group – Business Cards</title>
<link rel="stylesheet" href="https://fonts.googleapis.com/css2?family=Cinzel:wght@400;700&family=Great+Vibes&display=swap">
<style>
  :root {
    --deep-red: #b3202a;
    --ink: #1c1c1c;
    --gray-dark: #7d7d7d;
    --gray-mid: #a6a6a6;
    --white: #ffffff;
    --backdrop: #e9e6e5;
    --script-blue: #2a3f8f;
  }
  * { box-sizing: border-box; margin: 0; padding: 0; }
  html, body { width: 1200px; height: 840px; overflow: hidden; }
  body {
    background: var(--backdrop);
    font-family: "Cinzel", serif;
    position: relative;
  }
  .card {
    position: absolute;
    width: 665px;
    height: 380px;
    box-shadow: 0 8px 22px rgba(0,0,0,.35);
  }
  .card--front {
    left: 60px; top: 30px;
    background: linear-gradient(100deg, var(--white) 0%, var(--white) 38%, var(--gray-mid) 70%, var(--gray-dark) 100%);
  }
  .card--back {
    left: 475px; top: 430px;
    background: linear-gradient(90deg, var(--gray-dark) 0%, var(--gray-mid) 30%, var(--white) 62%, var(--white) 100%);
  }

  .brand {
    position: absolute;
    display: flex; align-items: center; gap: 10px;
    color: var(--ink); font-weight: 700; font-size: 28px; line-height: 1; white-space: nowrap;
  }
  .brand__mark { width: 18px; height: 18px; background: var(--deep-red); flex: none; }
  .card--front .brand { left: 50px; top: 160px; }
  .card--back .brand { right: 58px; top: 110px; }

  .contact {
    position: absolute; right: 40px; top: 36px;
    text-align: right; color: var(--white); font-size: 15px; line-height: 1.35;
  }
  .contact__name { color: var(--ink); font-weight: 700; font-size: 19px; }
  .contact__title { color: var(--ink); font-size: 15px; margin-bottom: 22px; }
  .contact__address { margin-bottom: 22px; }
  .contact__phones { margin-bottom: 26px; }

  .credential {
    position: absolute; left: 50px; bottom: 34px;
    color: var(--deep-red); font-weight: 700; font-size: 21px; letter-spacing: 1px;
  }

  .services {
    position: absolute; left: 24px; top: 90px;
    list-style: none; color: var(--white); font-weight: 700; font-size: 17px; line-height: 1.45; letter-spacing: .5px;
  }

  .follow { position: absolute; right: 58px; top: 200px; font-size: 17px; color: var(--deep-red); font-weight: 700; }
  .follow__lead { font-family: "Great Vibes", cursive; color: var(--script-blue); font-size: 24px; font-weight: 400; margin-right: 6px; }

  .social { position: absolute; right: 58px; top: 262px; display: flex; gap: 14px; list-style: none; }
  .social__item { display: flex; align-items: center; gap: 5px; font-size: 12px; font-weight: 700; color: var(--ink); }
  .social__mark { width: 12px; height: 12px; background: var(--gray-dark); }

  .site {
    position: absolute; right: 58px; bottom: 38px;
    color: var(--deep-red); font-weight: 700; font-size: 17px;
  }
</style>
</head>
<body>

  <section class="card card--front" aria-label="Card front">
    <div class="brand"><span class="brand__mark"></span>QDN Tech Group</div>
    <div class="contact">
      <p class="contact__name">Dana Whitfield</p>
      <p class="contact__title">President</p>
      <p class="contact__address">4820 Meridian Avenue<br>Suite 210<br>Easton, MD 21601</p>
      <p class="contact__phones">O.410.555.0142<br>F.410.555.0178<br>C.410.555.0193</p>
      <p class="contact__web">dana@qdntechgroup.com<br>www.qdntechgroup.com</p>
    </div>
    <p class="credential">Woman Owned Small Business</p>
  </section>

  <section class="card card--back" aria-label="Card back">
    <ul class="services">
      <li>Project Mgmt/Strategy</li>
      <li>Web App Development</li>
      <li>Mobile App</li>
      <li>Design</li>
      <li>Section 508</li>
      <li>Training</li>
      <li>Staffing</li>
      <li>Social Media</li>
      <li>Advertising</li>
      <li>Marketing</li>
    </ul>
    <div class="brand"><span class="brand__mark"></span>QDN Tech Group</div>
    <p class="follow"><span class="follow__lead">Follow us:</span>@QDNtechGroup</p>
    <ul class="social">
      <li class="social__item"><span class="social__mark"></span>Chatter</li>
      <li class="social__item"><span class="social__mark"></span>Chirp</li>
      <li class="social__item"><span class="social__mark"></span>Linkwork</li>
      <li class="social__item"><span class="social__mark"></span>Clipcast</li>
    </ul>
    <p class="site">www.QDNtechGroup.com</p>
  </section>

</body>
</html>
```